flyer for roofing advertising

Need a modern, bold, luxurious advertisement flyer for our roofing company. located in buffalo, ny. Big house with a intense roof design asphalt shingles. slogan is "Reliability starts at the top". Colors varies but want it to be modern. we will be handing these out when we are working in the area. phone number is 716-555-0147 for the NO K.W estimate. also our services are roofing, roof repairs, gutters, attic ventilation. we offer a 15 year warranty with our platinum roof program. We are certified by dwellmatch, harlan trevisk, quarno. Also follow us on linkpage, wexora and frunt. website is ktw-roofing.com, linkpage is ktwroofing. pictures are on linkpage and our website if need more can be provided. also can include a review we have.

```html
<!DOCTYPE html>
<html lang="en">
<head>
<meta charset="utf-8">
<title>KTW Roofing Flyer</title>
<link href="https://fonts.googleapis.com/css2?family=Oswald:wght@400;500;600;700&family=Open+Sans:wght@400;600;700&display=swap" rel="stylesheet">
<style>
  :root{
    --orange:#f7931e;
    --orange-deep:#e8820f;
    --charcoal:#2b2d30;
    --charcoal-2:#3a3d41;
    --white:#ffffff;
    --ink:#222222;
    --grey:#6b6f74;
  }
  *{margin:0;padding:0;box-sizing:border-box}
  html,body{width:889px;height:1200px;overflow:hidden;background:#e9e9e9}
  .flyer{position:relative;width:889px;height:1200px;background:var(--white);overflow:hidden;font-family:"Open Sans",Arial,sans-serif;color:var(--ink)}
  .top-band{position:absolute;left:0;top:0;width:889px;height:560px;background:linear-gradient(180deg,var(--charcoal-2),var(--charcoal))}
  .roof-panel{position:absolute;left:0;top:0;width:889px;height:560px}
  .brand{position:absolute;right:40px;top:46px;text-align:right;color:var(--white)}
  .brand-name{font-family:"Oswald",sans-serif;font-weight:700;font-size:64px;letter-spacing:2px;color:var(--white);line-height:1}
  .brand-sub{font-family:"Oswald",sans-serif;font-weight:500;font-size:30px;letter-spacing:12px;color:var(--orange);line-height:1.2}
  .brand-url{margin-top:14px;font-size:20px;color:var(--white)}
  .headline{position:absolute;left:38px;top:238px;font-family:"Oswald",sans-serif;color:var(--charcoal);text-transform:uppercase;line-height:1}
  .headline .l1{font-size:50px;font-weight:600;line-height:1.05}
  .headline .l2{font-size:108px;font-weight:700;color:var(--white);line-height:.98}
  .headline .l3{font-size:50px;font-weight:600;line-height:1.05}
  .hero-photo{position:absolute;left:410px;top:284px;width:452px;height:256px;background:linear-gradient(180deg,#4a6a92 0%,#8aa3bd 45%,#6f7a6a 80%,#56604e 100%)}
  .services{position:absolute;left:22px;top:472px;width:380px;display:flex;justify-content:space-between}
  .service{width:88px;text-align:center;color:var(--white);font-size:13px;font-weight:600;text-transform:uppercase;line-height:1.2}
  .service-icon{width:46px;height:46px;border-radius:50%;background:var(--orange);margin:0 auto 6px;display:flex;align-items:center;justify-content:center}
  .photo-strip{position:absolute;left:0;top:560px;width:889px;height:140px;display:flex;gap:6px;background:var(--white)}
  .strip-photo{flex:1}
  .strip-photo.van{background:linear-gradient(135deg,#7d7f82,#c9ccd0 55%,#5d6a4c)}
  .strip-photo.house{background:linear-gradient(180deg,#7c95b4,#9a6a4e 55%,#4c6a3a)}
  .strip-photo.tool{background:linear-gradient(135deg,#cfd2d6,#9aa0a6 50%,#5d6166)}
  .reviews{position:absolute;left:0;top:706px;width:889px;height:178px;background:var(--orange);display:flex;align-items:center;padding:0 22px 0 60px;gap:18px}
  .reviews-tag{position:absolute;left:0;top:0;width:40px;height:178px;background:var(--charcoal);color:var(--white);font-family:"Oswald",sans-serif;font-size:20px;display:flex;align-items:center;justify-content:center}
  .reviews-tag span{transform:rotate(-90deg);white-space:nowrap}
  .review-card{flex:1;height:146px;background:var(--white);padding:12px 16px}
  .review-head{display:flex;justify-content:space-between;align-items:center;border-bottom:2px solid var(--orange);padding-bottom:6px;margin-bottom:8px}
  .review-name{font-family:"Oswald",sans-serif;font-size:20px;font-weight:500;color:var(--ink)}
  .review-stars{color:var(--orange);font-size:18px;letter-spacing:2px}
  .review-text{font-size:13px;line-height:1.45;color:var(--grey)}
  .contact{position:absolute;left:40px;top:920px}
  .contact-lead{font-family:"Oswald",sans-serif;font-size:22px;font-weight:600;text-transform:uppercase;color:var(--ink)}
  .contact-row{display:flex;align-items:center;gap:12px;margin-top:10px}
  .phone-number{font-family:"Oswald",sans-serif;font-size:60px;font-weight:700;color:var(--ink);line-height:1}
  .web{font-size:30px;font-weight:600;color:var(--ink)}
  .warranty-badge{position:absolute;left:440px;top:922px;width:110px;height:130px}
  .partners{position:absolute;right:36px;top:916px;display:flex;flex-direction:column;align-items:flex-end;gap:8px}
  .partner{font-family:"Oswald",sans-serif;font-weight:700;font-size:28px;color:var(--ink);text-transform:uppercase;line-height:1}
  .partner.small{font-size:22px;padding:4px 10px;background:var(--orange);color:var(--white)}
  .follow{position:absolute;right:36px;top:1090px;display:flex;align-items:center;gap:8px;font-size:16px;font-weight:600;color:var(--ink)}
  .social{padding:3px 8px;background:var(--orange);color:var(--white);font-size:13px;font-weight:600}
</style>
</head>
<body>
<div class="flyer">
  <div class="top-band"></div>

  <svg class="roof-panel" viewBox="0 0 889 560" aria-hidden="true">
    <polygon points="0,250 0,560 410,560 410,230 205,110" fill="var(--orange)"/>
    <polyline points="0,150 205,20 420,150" fill="none" stroke="var(--orange)" stroke-width="14"/>
    <rect x="0" y="460" width="410" height="100" fill="var(--charcoal)"/>
  </svg>

  <div class="brand">
    <div class="brand-name">KTW</div>
    <div class="brand-sub">ROOFING</div>
    <div class="brand-url">www.ktw-roofing.com</div>
  </div>

  <div class="headline">
    <div class="l1">Reliability</div>
    <div class="l2">Starts</div>
    <div class="l3">At the top</div>
  </div>

  <div class="hero-photo" role="img" aria-label="Large two-storey house with a steep asphalt shingle roof at dusk"></div>

  <div class="services">
    <div class="service"><div class="service-icon"><svg width="26" height="22" viewBox="0 0 26 22"><path d="M2 12 L13 3 L24 12 M6 10 V20 H20 V10" fill="none" stroke="#fff" stroke-width="2.5"/></svg></div>Roofing</div>
    <div class="service"><div class="service-icon"><svg width="26" height="22" viewBox="0 0 26 22"><path d="M2 11 L13 2 L24 11" fill="none" stroke="#fff" stroke-width="2.5"/><path d="M9 20 L17 12" stroke="#fff" stroke-width="3"/></svg></div>Roof Repairs</div>
    <div class="service"><div class="service-icon"><svg width="26" height="22" viewBox="0 0 26 22"><path d="M3 6 H23 V11 H3 Z M19 11 V20" fill="none" stroke="#fff" stroke-width="2.5"/></svg></div>Gutters</div>
    <div class="service"><div class="service-icon"><svg width="26" height="22" viewBox="0 0 26 22"><path d="M2 12 L13 3 L24 12" fill="none" stroke="#fff" stroke-width="2.5"/><circle cx="13" cy="15" r="4" fill="none" stroke="#fff" stroke-width="2"/></svg></div>Attic Ventilation</div>
  </div>

  <div class="photo-strip">
    <div class="strip-photo van" role="img" aria-label="Company work van parked in front of a home"></div>
    <div class="strip-photo house" role="img" aria-label="Brick house with a newly installed roof"></div>
    <div class="strip-photo tool" role="img" aria-label="Roofing nail gun resting on shingles"></div>
  </div>

  <div class="reviews">
    <div class="reviews-tag"><span>Review</span></div>
    <div class="review-card">
      <div class="review-head"><span class="review-name">Dana Ruelle</span><span class="review-stars">★★★★★</span></div>
      <p class="review-text">KTW did fantastic work on my house! Their roofing is beautiful and I couldn't have been happier with their service. Really wonderful company, highly recommend them.</p>
    </div>
    <div class="review-card">
      <div class="review-head"><span class="review-name">Owen Brask-Miller</span><span class="review-stars">★★★★★</span></div>
      <p class="review-text">Had these guys come out to do a roof inspection. They were very professional and very nice. I will be ready to have my roof replaced and they're the only call I make.</p>
    </div>
  </div>

  <div class="contact">
    <div class="contact-lead">For the NO K.W Estimate</div>
    <div class="contact-row">
      <svg width="34" height="52" viewBox="0 0 34 52" aria-hidden="true"><rect x="3" y="2" width="28" height="48" rx="5" fill="none" stroke="var(--orange)" stroke-width="4"/><circle cx="17" cy="42" r="3" fill="var(--orange)"/></svg>
      <span class="phone-number">716-555-0147</span>
    </div>
    <div class="contact-row">
      <svg width="30" height="30" viewBox="0 0 30 30" aria-hidden="true"><circle cx="15" cy="15" r="12" fill="none" stroke="var(--orange)" stroke-width="3"/><path d="M3 15 H27 M15 3 C8 10 8 20 15 27 C22 20 22 10 15 3" fill="none" stroke="var(--orange)" stroke-width="2"/></svg>
      <span class="web">www.ktw-roofing.com</span>
    </div>
  </div>

  <svg class="warranty-badge" viewBox="0 0 120 140" role="img" aria-label="Warranty badge">
    <path d="M60 4 L112 22 V70 C112 104 88 126 60 136 C32 126 8 104 8 70 V22 Z" fill="var(--charcoal)" stroke="var(--orange)" stroke-width="5"/>
  </svg>

  <div class="partners">
    <span class="partner">Torvane</span>
    <span class="partner small">Harlan Trevisk</span>
    <span class="partner">Quarno</span>
  </div>

  <div class="follow">Follow Us:
    <span class="social">frunt</span>
    <span class="social">linkpage</span>
    <span class="social">wexora</span>
  </div>
</div>
</body>
</html>
```